Velmo BUSINESS CARD

Design an attention-grabbing business cards. Draw inspiration from the provided logo file. Please use the same font style as in the logo.
the back side of the card is for accent/decoration.

Contact Information for Business Card

PLEASE USE PROVIDED BUSINESS CARD SAMPLE

Other font styles liked:
• LUMETTE

Colors
EB3D1F
EC4F4E
F09395
F8D3D4
FCEDEE

Requirements
Must have
• RED, BLACK COLORS, SOLID BACK COLOR
Nice to have
• MAKE IT FANCY

```html
<!DOCTYPE html>
<html lang="en">
<head>
<meta charset="utf-8">
<title>Velmo Business Card</title>
<link href="https://fonts.googleapis.com/css2?family=Arimo:wght@400;700&display=swap" rel="stylesheet">
<style>
  :root {
    --page-bg: #e6e6e6;
    --card-bg: #2f2f2f;
    --card-panel: #262626;
    --accent-red: #eb3d1f;
    --ink-light: #ffffff;
    --ink-soft: #d9d9d9;
    --rule: #bdbdbd;
    --emblem-dark: #1c1c1c;
    --emblem-mid: #3a3a3a;
  }
  * { box-sizing: border-box; margin: 0; padding: 0; }
  html, body {
    width: 1200px; height: 802px; overflow: hidden;
    background: var(--page-bg);
    font-family: "Arimo", Arial, sans-serif;
  }
  .sheet {
    position: relative; width: 1200px; height: 802px;
    display: flex; align-items: center; justify-content: center; gap: 40px;
  }
  .card {
    position: relative; width: 540px; height: 309px;
    background: var(--card-bg); overflow: hidden;
    box-shadow: 0 6px 18px rgba(0,0,0,.25);
  }
  /* Front */
  .brand {
    position: absolute; right: 34px; top: 34px;
    display: flex; align-items: center; gap: 10px;
  }
  .brand-square {
    width: 34px; height: 34px; background: var(--accent-red);
    border: 3px solid var(--ink-light);
  }
  .brand-text { display: flex; flex-direction: column; }
  .brand-name {
    color: var(--ink-light); font-weight: 700; font-size: 40px;
    letter-spacing: 2px; line-height: 1;
  }
  .brand-tagline {
    color: var(--ink-soft); font-size: 7px; letter-spacing: 1.5px;
    margin-top: 3px; text-transform: uppercase;
  }
  .divider {
    position: absolute; left: 34px; right: 34px; top: 118px;
    height: 1px; background: var(--rule);
  }
  .person { position: absolute; left: 34px; top: 140px; }
  .person-name {
    color: var(--accent-red); font-weight: 700; font-size: 19px;
    text-transform: uppercase; letter-spacing: .5px;
  }
  .person-title { color: var(--ink-light); font-size: 13px; margin-top: 2px; }
  .person-rule {
    width: 150px; height: 1px; background: var(--rule); margin: 8px 0 8px;
  }
  .contact-list { list-style: none; }
  .contact-item {
    display: flex; align-items: center; gap: 9px;
    color: var(--ink-light); font-size: 13px; line-height: 20px;
  }
  .contact-icon { width: 11px; height: 11px; flex: none; }
  .address {
    position: absolute; right: 34px; top: 146px; text-align: right;
    color: var(--ink-light); font-size: 14px; line-height: 19px;
  }
  /* Back */
  .emblem-panel {
    position: absolute; left: 0; top: 0; bottom: 0; width: 216px;
    background: var(--card-panel);
    display: flex; align-items: center; justify-content: center;
  }
  .emblem-art {
    width: 180px; height: 180px; border-radius: 50%;
    background: radial-gradient(circle at 40% 35%, var(--emblem-mid), var(--emblem-dark));
  }
  .back-brand { position: absolute; left: 250px; top: 122px; }
  .back-name {
    color: var(--ink-light); font-weight: 700; font-size: 56px;
    letter-spacing: 3px; line-height: 1;
  }
  .back-tagline {
    color: var(--ink-soft); font-size: 10px; letter-spacing: 2px;
    margin-top: 6px; text-transform: uppercase;
  }
</style>
</head>
<body>
<main class="sheet">
  <section class="card card-front" aria-label="Business card front">
    <div class="brand">
      <span class="brand-square"></span>
      <div class="brand-text">
        <span class="brand-name">VELMO</span>
        <span class="brand-tagline">Logistics, refined</span>
      </div>
    </div>
    <div class="divider"></div>
    <div class="person">
      <p class="person-name">Owen Hale</p>
      <p class="person-title">President</p>
      <div class="person-rule"></div>
      <ul class="contact-list">
        <li class="contact-item">
          <svg class="contact-icon" viewBox="0 0 12 12"><path d="M2 1h3l1 3-2 1c.7 1.5 1.5 2.3 3 3l1-2 3 1v3c-5 .5-9.5-4-9-9z" fill="var(--accent-red)"/></svg>
          555-014-2291
        </li>
        <li class="contact-item">
          <svg class="contact-icon" viewBox="0 0 12 12"><rect x="2.5" y="0.5" width="7" height="11" rx="1" fill="none" stroke="var(--ink-light)"/><circle cx="6" cy="9.5" r=".7" fill="var(--ink-light)"/></svg>
          555-018-7736
        </li>
        <li class="contact-item">
          <svg class="contact-icon" viewBox="0 0 12 12"><rect x="0.5" y="2" width="11" height="8" fill="var(--accent-red)"/><path d="M.5 2 6 6.5 11.5 2" fill="none" stroke="var(--card-bg)"/></svg>
          OHale@velmo-llc.com
        </li>
        <li class="contact-item">
          <svg class="contact-icon" viewBox="0 0 12 12"><circle cx="6" cy="6" r="5.5" fill="var(--accent-red)"/><path d="M.5 6h11M6 .5c-2.5 3-2.5 8 0 11M6 .5c2.5 3 2.5 8 0 11" fill="none" stroke="var(--card-bg)" stroke-width=".8"/></svg>
          www.Velmo-LLC.com
        </li>
      </ul>
    </div>
    <p class="address">1480 N. 220 East<br>Fairview, IN, 46990</p>
  </section>

  <section class="card card-back" aria-label="Business card back">
    <div class="emblem-panel">
      <div class="emblem-art" role="img" aria-label="Embossed circular brand emblem, dark on dark"></div>
    </div>
    <div class="back-brand">
      <p class="back-name">VELMO</p>
      <p class="back-tagline">Logistics, refined</p>
    </div>
  </section>
</main>
</body>
</html>
```